Financial Advisor / Asset Manager Zup Design

I'm currently hosting with Zup and my first attempt at a website is live at www.ravenholtwealth.example Clearly I am not a web designer and I need help making this more catchy, modern, cross-platform compatible, search engine optimized, etc. I've got logos, hex color pallets, and a slew of other graphics. I'm interested in working with a winning designer to write/refine my copy/language to complete the build.

Full set of graphics https://pics.lumora-share.example/q71TzR05KwPd2MhXN do NOT use the CONSULTING graphics as this is for a related business / different website

Target Market(s)

Individuals, small institutions, endowments, non-profits seeking financial advice and asset / portfolio management

Industry/Entity Type

Financial Services

Coding

Coded - Design and coding required

Font styles to use
Other font styles liked:
• AvenirLTStd - Black, Book, and Roman as appropriate

Requirements
Must have
• Complete, cross platform website integrating my existing logo
Nice to have
• Easy to update format for go-forward maintenance

```html
<!DOCTYPE html>
<html lang="en">
<head>
<meta charset="utf-8">
<title>Ravenholt Wealth — Personalized Financial Advice</title>
<link href="https://fonts.googleapis.com/css2?family=Nunito+Sans:wght@400;600;700;800;900&display=swap" rel="stylesheet">
<style>
:root{
  --blue:#1474c4;
  --blue-dark:#0d5ea6;
  --blue-light:#7cb8e4;
  --navy:#1d2535;
  --ink:#222733;
  --text:#4a4f59;
  --pale:#eef2f8;
  --white:#ffffff;
  --dark:#222222;
}
*{margin:0;padding:0;box-sizing:border-box}
html,body{width:1200px;height:3390px;overflow:hidden}
body{font-family:"Nunito Sans",Arial,sans-serif;color:var(--text);background:var(--white);position:relative}
.abs{position:absolute}
a{color:inherit;text-decoration:none}

/* header + hero */
.hero{left:0;top:0;width:1200px;height:645px;overflow:hidden}
.hero-photo{left:0;top:0;width:1200px;height:645px;background:linear-gradient(180deg,#7d8ea3 0%,#b07a52 22%,#8a5a3c 38%,#4b3d33 55%,#1e2a22 75%,#101a15 100%)}
.brand{left:171px;top:40px;color:var(--white);font-weight:700;font-size:19px;letter-spacing:1px;line-height:1.1;text-align:center;width:120px}
.brand small{display:block;font-size:10px;letter-spacing:3px;font-weight:700}
.nav{left:429px;top:30px;display:flex;gap:42px;color:#e8eef5;font-size:15px;font-weight:600}
.nav .active{color:var(--white);border-bottom:2px solid var(--blue);padding-bottom:4px}
.nav-phone{left:873px;top:21px;width:153px;height:38px;background:var(--blue);border-radius:6px;color:var(--white);font-weight:800;font-size:14px;display:flex;align-items:center;justify-content:center;gap:10px}
.hero-copy{left:231px;top:145px;color:var(--white)}
.hero-copy .lead{font-size:40px;font-weight:400;line-height:1}
.hero-copy h1{font-size:80px;font-weight:900;line-height:.98;margin-top:8px}
.btn{display:inline-flex;align-items:center;gap:8px;background:var(--blue);color:var(--white);font-weight:800;text-transform:uppercase;border-radius:24px 0 24px 24px}
.hero-btn{left:220px;top:368px;width:167px;height:46px;justify-content:center;font-size:16px}
.arrow{color:var(--white)}

/* features */
.feature{top:684px;width:256px;height:254px;background:var(--blue);border-radius:0 128px 128px 128px;color:var(--white);text-align:center}
.feature::after{content:"";position:absolute;left:12px;top:12px;right:12px;bottom:12px;border:2px solid rgba(255,255,255,.8);border-radius:0 116px 116px 116px}
.feature svg{margin-top:44px}
.feature h3{font-size:17px;font-weight:800;margin-top:8px}
.feature p{font-size:14px;line-height:1.7;margin:4px auto 0;width:200px}

/* about */
.about{left:0;top:967px;width:1200px;height:511px;background:var(--pale)}
.eyebrow{left:173px;top:1022px;color:var(--blue);font-size:22px;letter-spacing:1px}
.about h2{left:173px;top:1046px;color:var(--ink);font-size:50px;font-weight:900;line-height:1.12;width:300px}
.about-text{left:172px;top:1168px;width:290px;font-size:16px;line-height:1.65}
.about-btn{left:172px;top:1339px;width:168px;height:47px;justify-content:center;font-size:15px;gap:14px}
.about-photo{left:448px;top:1033px;width:628px;height:306px;background:linear-gradient(180deg,var(--pale) 0%,#cfe0f0 40%,#9bb5cc 70%,#6b7b8c 100%)}

/* services */
.services{left:0;top:1478px;width:1200px;height:617px;background:linear-gradient(180deg,#1a6fc2 0%,#1b7ad0 55%,#1574c6 100%)}
.services h2{left:0;top:1553px;width:1200px;text-align:center;color:var(--white);font-size:50px;font-weight:900}
.service{top:1632px;width:270px;color:var(--white)}
.service .photo{width:270px;height:201px;border:2px solid rgba(255,255,255,.7);border-radius:0 30px 0 30px;padding:8px 8px 0 0}
.service .photo div{width:100%;height:100%;border-radius:0 0 0 26px}
.service h3{font-size:20px;font-weight:700;margin-top:18px}
.service p{font-size:16px;line-height:1.4;margin-top:10px;width:265px}
.ghost{display:inline-flex;align-items:center;gap:10px;border:2px solid var(--white);border-radius:20px 0 20px 20px;height:37px;padding:0 20px;font-size:13px;font-weight:800;margin-top:18px}

/* faqs */
.faqs-title{left:0;top:2160px;width:1200px;text-align:center;color:var(--ink);font-size:50px;font-weight:900}
.faq{width:418px;height:55px;border:2px solid var(--blue);display:flex;align-items:center;justify-content:space-between;padding:0 12px;font-size:15px;color:var(--ink)}
.faq span b{font-weight:800}
.faq i{flex:none;width:17px;height:17px;border-radius:50%;background:var(--blue);display:flex;align-items:center;justify-content:center}
.ring{border-radius:50%;border:18px solid #e4eef8}

/* contact */
.contact{left:0;top:2511px;width:1200px;height:595px;background:linear-gradient(180deg,#3e4a58 0%,#27303a 40%,#1a2430 70%,#111820 100%)}
.contact h2{left:0;top:2598px;width:1200px;text-align:center;color:var(--white);font-size:35px;font-weight:800}
.field{background:var(--white);height:40px;color:#707070;font-size:16px;padding:11px 14px}
.submit{left:529px;top:2862px;width:141px;height:40px;border:2px solid var(--white);border-radius:20px 0 20px 20px;color:var(--white);font-weight:800;font-size:14px;display:flex;align-items:center;justify-content:center;gap:10px}

/* footer */
.footer{left:0;top:3106px;width:1200px;height:284px;background:var(--dark);color:#e6e6e6}
.foot-brand{left:171px;top:3178px;width:178px;color:var(--blue);font-size:26px;font-weight:700;letter-spacing:1px;text-align:center;line-height:1.15}
.foot-brand small{display:block;font-size:15px;letter-spacing:4px}
.social{top:3272px;width:34px;height:34px;border:2px solid #dcdcdc}
.foot-h{top:3136px;font-size:17px;font-weight:800;color:var(--white)}
.foot-txt{font-size:14px;line-height:1.45}
.links{left:647px;top:3172px;font-size:14px;display:flex;flex-direction:column;gap:18px}
.news-input{left:791px;top:3183px;width:237px;height:38px;background:var(--white);color:#888;font-size:12px;display:flex;align-items:center;gap:8px;padding-left:12px}
.news-btn{left:792px;top:3228px;width:236px;height:38px;background:var(--blue);border-radius:19px 0 19px 19px;color:var(--white);font-weight:800;font-size:15px;display:flex;align-items:center;justify-content:center}
.copy{left:783px;top:3316px;font-size:12px}
.copy b{color:var(--blue);font-weight:700}
</style>
</head>
<body>

<section class="hero abs">
  <div class="hero-photo abs" role="img" aria-label="Photograph of sunlit rocky mountain peaks above a dark pine forest"></div>
  <svg class="abs" style="left:0;top:0" width="1200" height="645" viewBox="0 0 1200 645">
    <polygon points="0,610 600,516 1200,610 1200,645 0,645" fill="var(--blue)"/>
    <polygon points="0,632 600,523 1200,632 1200,645 0,645" fill="#fff"/>
    <polyline points="172,230 198,255 172,280" transform="translate(370,0) scale(-1,1) translate(-198,0)" fill="none" stroke="#fff" stroke-width="2"/>
    <polyline points="1000,230 1025,255 1000,280" fill="none" stroke="#fff" stroke-width="2"/>
  </svg>
</section>

<header>
  <div class="brand abs">RAVENHOLT<small>WEALTH</small></div>
  <nav class="nav abs">
    <a class="active">Home</a><a>About</a><a>FAQs</a><a>Services</a><a>Contact</a>
  </nav>
  <a class="nav-phone abs">
    <svg width="14" height="14" viewBox="0 0 24 24"><path fill="#fff" d="M6.6 10.8a15 15 0 0 0 6.6 6.6l2.2-2.2c.3-.3.7-.4 1-.2 1.1.4 2.3.6 3.6.6.6 0 1 .4 1 1V20c0 .6-.4 1-1 1A17 17 0 0 1 3 4c0-.6.4-1 1-1h3.5c.6 0 1 .4 1 1 0 1.3.2 2.5.6 3.6.1.3 0 .7-.2 1z"/></svg>
    (555) 014-2290
  </a>
</header>

<div class="hero-copy abs">
  <p class="lead">Personalized</p>
  <h1>Financial<br>Advice</h1>
</div>
<a class="btn hero-btn abs">Know More ›</a>

<section class="features">
  <svg class="abs" style="left:162px;top:790px" width="20" height="30" viewBox="0 0 20 30"><polyline points="16,2 4,15 16,28" fill="none" stroke="#333" stroke-width="4"/></svg>
  <svg class="abs" style="left:1020px;top:790px" width="20" height="30" viewBox="0 0 20 30"><polyline points="4,2 16,15 4,28" fill="none" stroke="#333" stroke-width="4"/></svg>

  <div class="feature abs" style="left:195px">
    <svg width="56" height="56" viewBox="0 0 56 56" fill="none" stroke="#fff" stroke-width="2"><circle cx="30" cy="32" r="17"/><circle cx="30" cy="32" r="12"/><path d="M30 32V23M30 32l6 4M26 10h8M30 10v5M4 28h8M2 34h10M6 40h8"/></svg>
    <h3>You Come First</h3>
    <p>We always act in the best interests of our clients</p>
  </div>
  <div class="feature abs" style="left:474px">
    <svg width="60" height="56" viewBox="0 0 60 56" fill="none" stroke="#fff" stroke-width="2"><rect x="8" y="6" width="44" height="32"/><circle cx="30" cy="20" r="7"/><path d="M14 14h8M14 20h8M14 26h8M38 14h8M38 20h8M38 26h8M28 30v18l4-4 4 8"/></svg>
    <h3>Personalized Services</h3>
    <p>We get to know you in order to service your unique needs</p>
  </div>
  <div class="feature abs" style="left:751px">
    <svg width="56" height="56" viewBox="0 0 56 56" fill="none" stroke="#fff" stroke-width="2"><path d="M12 4h24l8 8v36H12z"/><path d="M18 14h14M18 20h18M18 26h10M18 32h10"/><circle cx="38" cy="38" r="7"/><path d="M43 43l8 8"/></svg>
    <h3>Transparent Fees</h3>
    <p>You'll always know what you pay and how we get paid</p>
  </div>
</section>

<section class="about abs"></section>
<p class="eyebrow abs">ABOUT</p>
<h2 class="abs" style="left:173px;top:1046px;color:var(--ink);font-size:50px;font-weight:900;line-height:1.12;width:300px">Ravenholt Wealth</h2>
<p class="about-text abs">Ravenholt Wealth is a registered investment advisory firm committed to serving as fiduciary to our clients. We always act in the best interests of our clients, including putting your interests ahead of our own.</p>
<a class="btn about-btn abs">Read More <span>›</span></a>
<div class="about-photo abs" role="img" aria-label="Photograph of three advisors reviewing a laptop together in front of a light blue mountain outline"></div>

<section class="services abs"></section>
<h2 class="abs" style="left:0;top:1553px;width:1200px;text-align:center;color:#fff;font-size:50px;font-weight:900">Our Services</h2>

<article class="service abs" style="left:171px">
  <div class="photo"><div role="img" aria-label="Photograph of a businessman beside a glowing blue bar chart" style="background:linear-gradient(135deg,#0b3f8f,#2a8ae0 50%,#0a3276)"></div></div>
  <h3>Stock Selection</h3>
  <p>Many advisors use a screening process to find investments. You may be familiar with stock</p>
  <a class="ghost">READ MORE ›</a>
</article>
<article class="service abs" style="left:467px">
  <div class="photo"><div role="img" aria-label="Photograph of a hand ticking a checklist box with a pen" style="background:linear-gradient(135deg,#0f5fae,#1677c9 60%,#0a3f7a)"></div></div>
  <h3>Alternatives</h3>
  <p>The challenges facing investors seeking to build portfolios capable of generating attractive returns</p>
  <a class="ghost">READ MORE ›</a>
</article>
<article class="service abs" style="left:762px">
  <div class="photo"><div role="img" aria-label="Photograph of a hand turning the pages of a report" style="background:linear-gradient(135deg,#e8e4df,#cfc7bd 50%,#f2f2f2)"></div></div>
  <h3>Optimization</h3>
  <p>Your investment portfolio was built with money you earned. It should be customized to reflect your goals</p>
  <a class="ghost">READ MORE ›</a>
</article>

<section class="faqs">
  <div class="ring abs" style="left:-90px;top:2010px;width:240px;height:200px;border-color:#e8f0f9"></div>
  <div class="ring abs" style="left:1055px;top:2330px;width:220px;height:220px;border-color:#e8f0f9"></div>
  <h2 class="faqs-title abs">FAQs</h2>
  <div class="faq abs" style="left:180px;top:2237px"><span><b>Q.</b> What is a registered investment advisor? Are you a registered investment advisor?</span><i><svg width="8" height="8" viewBox="0 0 8 8"><polyline points="2,1 6,4 2,7" fill="none" stroke="#fff" stroke-width="1.6"/></svg></i></div>
  <div class="faq abs" style="left:601px;top:2237px"><span><b>Q.</b> What is a custodian? Are you a custodian?</span><i><svg width="8" height="8" viewBox="0 0 8 8"><polyline points="2,1 6,4 2,7" fill="none" stroke="#fff" stroke-width="1.6"/></svg></i></div>
  <div class="faq abs" style="left:180px;top:2296px"><span><b>Q.</b> What is a fiduciary? Are you a fiduciary?</span><i><svg width="8" height="8" viewBox="0 0 8 8"><polyline points="2,1 6,4 2,7" fill="none" stroke="#fff" stroke-width="1.6"/></svg></i></div>
  <div class="faq abs" style="left:601px;top:2296px"><span><b>Q.</b> How often will we meet? How will you keep me informed?</span><i><svg width="8" height="8" viewBox="0 0 8 8"><polyline points="2,1 6,4 2,7" fill="none" stroke="#fff" stroke-width="1.6"/></svg></i></div>
  <div class="faq abs" style="left:180px;top:2356px"><span><b>Q.</b> What are your fees? How much will I pay?</span><i><svg width="8" height="8" viewBox="0 0 8 8"><polyline points="2,1 6,4 2,7" fill="none" stroke="#fff" stroke-width="1.6"/></svg></i></div>
  <div class="faq abs" style="left:601px;top:2356px"><span><b>Q.</b> What is a custodian? Are you a custodian?</span><i><svg width="8" height="8" viewBox="0 0 8 8"><polyline points="2,1 6,4 2,7" fill="none" stroke="#fff" stroke-width="1.6"/></svg></i></div>
</section>

<section class="contact abs" role="img" aria-label="Photograph of a dark mountain lake at dusk reflecting snowy peaks"></section>
<h2 class="abs" style="left:0;top:2598px;width:1200px;text-align:center;color:#fff;font-size:35px;font-weight:800">Get In Touch</h2>
<form>
  <div class="field abs" style="left:236px;top:2658px;width:359px">First Name</div>
  <div class="field abs" style="left:605px;top:2658px;width:360px">Last Name</div>
  <div class="field abs" style="left:236px;top:2703px;width:359px">Email</div>
  <div class="field abs" style="left:605px;top:2703px;width:360px">Phone</div>
  <div class="field abs" style="left:236px;top:2754px;width:729px;height:86px">Your Message</div>
  <div class="submit abs">SUBMIT ›</div>
</form>

<svg class="abs" style="left:0;top:2975px" width="1200" height="135" viewBox="0 0 1200 135">
  <polygon points="0,105 600,0 1200,105 1200,135 0,135" fill="#fff"/>
  <polygon points="0,117 600,8 1200,117 1200,135 0,135" fill="var(--dark)"/>
</svg>

<footer class="footer abs"></footer>
<div class="foot-brand abs">RAVENHOLT<small>WEALTH</small></div>
<div class="social abs" style="left:171px"></div>
<div class="social abs" style="left:214px"></div>
<div class="social abs" style="left:257px"></div>

<h4 class="foot-h abs" style="left:397px">Contact Us</h4>
<div class="abs foot-txt" style="left:395px;top:3170px;display:flex;gap:6px">
  <svg width="10" height="14" viewBox="0 0 10 14"><path d="M5 0a5 5 0 0 1 5 5c0 4-5 9-5 9S0 9 0 5a5 5 0 0 1 5-5z" fill="var(--blue)"/><circle cx="5" cy="5" r="2" fill="var(--dark)"/></svg>
  <span>1820 Alder Ridge Rd, Suite #240<br>Fairhollow, VA 20000</span>
</div>
<div class="abs foot-txt" style="left:395px;top:3224px;display:flex;gap:6px;align-items:center">
  <svg width="12" height="12" viewBox="0 0 24 24"><path fill="var(--blue)" d="M6.6 10.8a15 15 0 0 0 6.6 6.6l2.2-2.2c.3-.3.7-.4 1-.2 1.1.4 2.3.6 3.6.6.6 0 1 .4 1 1V20c0 .6-.4 1-1 1A17 17 0 0 1 3 4c0-.6.4-1 1-1h3.5c.6 0 1 .4 1 1 0 1.3.2 2.5.6 3.6.1.3 0 .7-.2 1z"/></svg>
  <span>(555) 014-2290</span>
</div>

<h4 class="foot-h abs" style="left:647px">Quick Links</h4>
<nav class="links abs"><a>Home</a><a>About</a><a>FAQs</a><a>Services</a><a>Contact</a></nav>

<h4 class="foot-h abs" style="left:790px">Newsletter</h4>
<div class="news-input abs">
  <svg width="13" height="10" viewBox="0 0 13 10"><rect width="13" height="10" fill="#999"/><polyline points="0,0 6.5,5 13,0" fill="none" stroke="#fff"/></svg>
  Enter email Address
</div>
<div class="news-btn abs">SUBSCRIBE</div>
<p class="copy abs">© 2022 <b>Ravenholt Wealth.</b> All right reserved</p>

</body>
</html>
```